International Property Consultancy

Brief Overview:

I need a dynamic and well designed website that is easy to use and understand. It has to be unique and different to generic templates that most websites seem to be these days. PLEASE NO GENERIC TEMPLATES FROM THE INTERNET.

Our business has 10 years experience working on struggling international developments that we then work in-house for to turn around and brings bout success. We stay within a project often for long periods of time until success is achieved. We are unique in our approach and completely different to the standard routes to market for many developments. The site is for developers to see what we have done in regards to previous projects, as such we want to incorporate video into this site with a strong design aesthetic. There will be videos of the past projects we have worked on, which will act as case studies.

I like very simple but punchy websites, that people can navigate and understand very easily. Also a big fan of unique and well thought out design aesthetic.

Initial Site layout thoughts:

1) Homepage:
2) About Us
3) What we've done / Work
This part has the projects we have worked on (France, Portugal, London, Morocco). Each one will have some video content and photo images, but also would be good to have a succinct way to mention what we did and the successes in a clever and punchy way.

4) Contact Us

* This is just a guideline. Would be open to input and creative direction on your own part.

*More details and websites we like can be seen in the brief doc attached.

PLEASE VIEW THE WIREFRAME WORD DOC ATTACHED.

Here there are also some more examples to help:

Here are just a few examples of websites and what I like about them:

- www.velmoro.com (clean, nice geometric design aesthetic, good animation when loading and changing pages well thought out all though also coulee be considered a bit dull and basic after the initial homepage slide)
- https://www.farbridgehub.net (Clean site, quite clinical, lacks video content and doesn't engage greatly).
- https://ruskotile.com (minimal, and like how it mixes the design aesthetic more with video and photo content)

- https://www.amberquillworks.com (like the layout of this and how it displays the projects and work section)

- https://brisk.com (Good use of video content)

- https://loomfield.studio (minimal to the point and mixes design with video and animation etc...)

Here is another couple of cool websites that may help give you some direction: https://halvenquay.com www.brisk.com

Hi there, One of the things I thought would be good on the homepage is to add the logo with a 'digital landscape' before flicking down into a slide with video content of the projects... Just an idea but have posted some pics in the brief. We would get this animated for the site. But if you have better ideas, please do run with them. Thanks,

Target Market(s)

Property developers

Number of Pages Required

4 page

Font styles to use
Other font styles liked:
• Read brief

Requirements
Must have
• Needs to be clean, dynamic and easy to follow on desktop and mobile. We will use it as a kind of portfolio website so will need to embed video of past projects we have worked on.

Read brief in docs.
Nice to have
• Clean
Should not have
• Not be another generic template website.
Not have random property stock photos. (We are not a property agency).

```html
<!DOCTYPE html>
<html lang="en">
<head>
<meta charset="utf-8">
<title>Talvenor — International Property Developments</title>
<link href="https://fonts.googleapis.com/css2?family=Work+Sans:wght@200;400;500;600;700;800&display=swap" rel="stylesheet">
<style>
  :root {
    --ink: #1e1e1e;
    --ink-soft: #333333;
    --paper: #ffffff;
    --map-light: #f4f4f4;
    --map-mid: #e2e2e2;
    --footer-bg: #1e1e1e;
    --footer-text: #f2f2f2;
    --footer-rule: #5a5a5a;
  }
  * { margin: 0; padding: 0; box-sizing: border-box; }
  html, body { width: 1040px; height: 1200px; overflow: hidden; background: var(--paper); }
  body { font-family: "Work Sans", Arial, sans-serif; color: var(--ink); }

  .page { position: relative; width: 1040px; height: 1200px; overflow: hidden; }

  .corner-ornament { position: absolute; left: 730px; top: 0; width: 310px; height: 235px; background: var(--ink-soft); border-bottom-left-radius: 170px 200px; border-top-left-radius: 40px 60px; }

  .brand { position: absolute; left: 158px; top: 12px; font-size: 36px; font-weight: 500; letter-spacing: -0.6px; color: var(--ink); }

  .menu-toggle { position: absolute; left: 848px; top: 18px; width: 34px; text-align: center; color: var(--paper); font-size: 9.5px; font-weight: 500; letter-spacing: 0.3px; }
  .menu-toggle .bar { display: block; height: 1px; background: var(--paper); margin: 0 auto 2px; }
  .menu-toggle .bar.long { width: 24px; }
  .menu-toggle .bar.short { width: 16px; margin-bottom: 5px; }

  .hero-eyebrow { position: absolute; left: 160px; top: 124px; font-size: 13px; letter-spacing: 2.3px; font-weight: 400; }
  .hero-title { position: absolute; left: 158px; top: 146px; font-size: 39px; line-height: 42px; font-weight: 800; letter-spacing: 0.2px; text-transform: uppercase; }
  .hero-title .thin { font-weight: 200; }

  .video-card { position: absolute; left: 159px; top: 314px; width: 722px; height: 389px; background: var(--paper); box-shadow: 0 4px 14px rgba(0,0,0,0.08); overflow: hidden; }
  .video-card .world-map { position: absolute; inset: 0; background: radial-gradient(ellipse at 50% 45%, var(--map-mid) 0%, var(--map-light) 55%, var(--paper) 100%); }
  .play-button { position: absolute; left: 320px; top: 128px; }
  .video-caption { position: absolute; left: 0; right: 0; top: 323px; text-align: center; font-size: 12px; line-height: 13px; letter-spacing: 0.4px; }
  .video-caption strong { display: block; font-weight: 700; }

  .slide-pager { position: absolute; left: 440px; top: 726px; }
  .slide-pager .num { position: absolute; top: 20px; width: 20px; margin-left: -10px; text-align: center; font-size: 12px; font-weight: 700; }

  .slide-eyebrow { position: absolute; left: 159px; top: 780px; font-size: 13.5px; letter-spacing: 2px; font-weight: 400; }
  .slide-title { position: absolute; left: 158px; top: 793px; font-size: 24.5px; font-weight: 800; letter-spacing: 0.8px; }
  .cta { position: absolute; left: 159px; top: 834px; width: 136px; height: 38px; background: var(--ink); color: var(--paper); font-size: 10px; font-weight: 600; letter-spacing: 1.5px; display: flex; align-items: center; justify-content: center; gap: 9px; }

  .site-footer { position: absolute; left: 0; top: 924px; width: 1040px; height: 276px; background: var(--footer-bg); color: var(--footer-text); }
  .footer-brand { position: absolute; left: 0; right: 0; top: 14px; text-align: center; font-size: 36px; font-weight: 500; letter-spacing: -0.6px; }
  .footer-rule { position: absolute; height: 1px; background: var(--footer-text); }
  .contact-col { position: absolute; top: 104px; }
  .contact-col h3 { font-size: 12px; font-weight: 400; letter-spacing: 1px; display: flex; align-items: center; gap: 6px; }
  .contact-col h3 b { font-weight: 700; }
  .contact-col h3::after { content: ""; width: 31px; height: 1px; background: var(--footer-text); }
  .contact-item { display: flex; gap: 9px; margin-top: 14px; font-size: 10px; line-height: 13.5px; letter-spacing: 0.3px; }
  .contact-item svg { flex: none; margin-top: 1px; }
  .social-row { position: absolute; left: 465px; top: 194px; width: 110px; height: 35px; border-top: 1px solid var(--footer-rule); border-bottom: 1px solid var(--footer-rule); display: flex; align-items: center; justify-content: space-around; font-size: 8px; font-weight: 600; letter-spacing: 0.3px; }
  .copyright { position: absolute; left: 0; right: 0; top: 245px; text-align: center; font-size: 9.5px; letter-spacing: 0.2px; }
</style>
</head>
<body>
<div class="page">

  <div class="corner-ornament" role="img" aria-label="Dark abstract shape with light geometric accents"></div>

  <div class="brand">talvenor.</div>

  <div class="menu-toggle">
    <span class="bar long"></span><span class="bar short"></span>MENU
  </div>

  <p class="hero-eyebrow">WE ARE TALVENOR</p>
  <h1 class="hero-title">We fulfill international<br>property <span class="thin">developments</span></h1>

  <section class="video-card">
    <div class="world-map" role="img" aria-label="Dotted world map overlaid with a network of connected points"></div>
    <svg class="play-button" width="82" height="82" viewBox="0 0 82 82" aria-label="Play video">
      <circle cx="41" cy="41" r="40" fill="#5a5a5a" opacity="0.9"/>
      <circle cx="41" cy="41" r="34" fill="#8a8a8a"/>
      <circle cx="41" cy="41" r="27" fill="#0f0f0f"/>
      <path d="M35 30 L53 41 L35 52 Z" fill="var(--paper)"/>
    </svg>
    <p class="video-caption">CLICK ABOVE<strong>SEE THE VIDEO</strong></p>
  </section>

  <div class="slide-pager">
    <svg width="160" height="16" viewBox="0 0 160 16" aria-hidden="true">
      <line x1="16" y1="7" x2="44" y2="7" stroke="var(--ink)" stroke-width="0.7"/>
      <line x1="63" y1="7" x2="90" y2="7" stroke="var(--ink)" stroke-width="0.7"/>
      <line x1="109" y1="7" x2="137" y2="7" stroke="var(--ink)" stroke-width="0.7"/>
      <circle cx="10" cy="7" r="5.5" fill="var(--ink)"/>
      <circle cx="57" cy="7" r="5.5" fill="none" stroke="var(--ink)" stroke-width="1"/>
      <circle cx="103" cy="7" r="5.5" fill="none" stroke="var(--ink)" stroke-width="1"/>
      <circle cx="150" cy="7" r="5.5" fill="none" stroke="var(--ink)" stroke-width="1"/>
    </svg>
    <span class="num" style="left:10px">1</span>
    <span class="num" style="left:57px">2</span>
    <span class="num" style="left:103px">3</span>
    <span class="num" style="left:150px">4</span>
  </div>

  <p class="slide-eyebrow">LOREM IPSUM DOLAR</p>
  <h2 class="slide-title">LOREM IPSUM DOLAR SIT AMET</h2>
  <a class="cta">VIEW RESULT
    <svg width="10" height="10" viewBox="0 0 10 10" aria-hidden="true"><circle cx="5" cy="5" r="5" fill="var(--paper)"/><path d="M4 2.8 L6.2 5 L4 7.2" fill="none" stroke="var(--ink)" stroke-width="1.4"/></svg>
  </a>

  <footer class="site-footer">
    <div class="footer-brand">talvenor.</div>
    <span class="footer-rule" style="left:455px;top:65px;width:130px"></span>
    <span class="footer-rule" style="left:485px;top:71px;width:70px"></span>

    <div class="contact-col" style="left:212px">
      <h3>OUR <b>ADDRESS</b></h3>
      <div class="contact-item">
        <svg width="10" height="14" viewBox="0 0 10 14" aria-hidden="true"><path d="M5 0 A5 5 0 0 1 10 5 C10 8 5 14 5 14 C5 14 0 8 0 5 A5 5 0 0 1 5 0 Z" fill="var(--footer-text)"/><circle cx="5" cy="5" r="1.8" fill="var(--footer-bg)"/></svg>
        <p>Lorem Ipsum dolar sit amet<br>Lorem Ipsum dolar</p>
      </div>
    </div>

    <div class="contact-col" style="left:449px">
      <h3>OUR <b>PHONE NO</b></h3>
      <div class="contact-item">
        <svg width="16" height="16" viewBox="0 0 16 16" aria-hidden="true"><path d="M3 1 L6 4 L4.5 6 C5.5 8 8 10.5 10 11.5 L12 10 L15 13 L13 15 C7 15 1 9 1 3 Z" fill="var(--footer-text)"/><path d="M9 3 A4 4 0 0 1 13 7 M9 0.8 A6.2 6.2 0 0 1 15.2 7" fill="none" stroke="var(--footer-text)" stroke-width="1"/></svg>
        <p>Call Us:<br>123-456-7890</p>
      </div>
    </div>

    <div class="contact-col" style="left:660px">
      <h3>OUR <b>MAIL ADDRESS</b></h3>
      <div class="contact-item">
        <svg width="15" height="11" viewBox="0 0 15 11" aria-hidden="true" style="margin-top:6px"><rect x="0.5" y="0.5" width="14" height="10" fill="none" stroke="var(--footer-text)"/><path d="M0.5 0.5 L7.5 6 L14.5 0.5 M0.5 10.5 L5.5 5 M14.5 10.5 L9.5 5" fill="none" stroke="var(--footer-text)"/></svg>
        <p>Mail Us:<br>talvenor@domain.com</p>
      </div>
    </div>

    <nav class="social-row" aria-label="Social channels">
      <span>Share</span><span>Post</span><span>Pics</span><span>Work</span>
    </nav>

    <p class="copyright">Copyright © 2020 Talvenor. All Rights Reserved.</p>
  </footer>

</div>
</body>
</html>
```